Skyward Rovers

I would like to re-fresh my existing web page with something more elegant and professional and what will match with my new logo. From the page it should be clearly seen that I organize and sell flying safaris, it should not be tightened only to Africa, should be general.

Page to be re-freshed:
http://skyward-rovers.example

Target Market(s)

Pilots and non-pilots who are going to have a bush flying safari in Africa

Industry/Entity Type

It Professional

```html
<!DOCTYPE html>
<html lang="en">
<head>
<meta charset="utf-8">
<title>Skyward Rovers – Flying Safaris</title>
<link rel="stylesheet" href="https://fonts.googleapis.com/css2?family=Asap+Condensed:wght@400;500&family=PT+Sans:wght@400;700&display=swap">
<style>
  :root {
    --yellow: #f2d000;
    --black: #000;
    --nav-dark: #333333;
    --text-light: #ffffff;
    --text-dark: #1a1a1a;
    --hero-bar: #5c5c5c;
    --panel: rgba(60, 55, 50, 0.72);
    --red: #e02020;
    --grass-a: #b98a45;
    --grass-b: #7d6a3a;
  }
  * { margin: 0; padding: 0; box-sizing: border-box; }
  html, body { width: 1037px; height: 1200px; overflow: hidden; }
  body {
    position: relative;
    background: var(--black);
    font-family: "PT Sans", sans-serif;
    color: var(--text-light);
  }
  .abs { position: absolute; }

  /* header */
  .site-header { left: 0; top: 0; width: 1037px; height: 111px; background: var(--yellow); }
  .brand { left: 96px; top: 28px; display: flex; align-items: center; gap: 12px; }
  .brand-mark { width: 40px; height: 40px; border-radius: 50%; background: var(--text-dark); }
  .brand-name { font-family: "Asap Condensed", sans-serif; font-size: 38px; font-weight: 400; color: var(--text-dark); letter-spacing: 0.5px; }
  .book-note { right: 93px; top: 36px; font-size: 11px; color: var(--text-dark); }
  .book-button {
    left: 825px; top: 54px; width: 117px; height: 27px;
    background: #555; color: #fff; border-radius: 3px;
    font-family: "Asap Condensed", sans-serif; font-size: 16px;
    display: flex; align-items: center; justify-content: center;
    box-shadow: 0 1px 2px rgba(0,0,0,0.4);
  }

  /* navigation */
  .main-nav { left: 0; top: 111px; width: 1037px; height: 32px; background: var(--nav-dark); }
  .nav-rule { left: 0; top: 143px; width: 1037px; height: 9px; background: var(--yellow); }
  .nav-item {
    top: 111px; width: 170px; height: 32px;
    display: flex; align-items: center; justify-content: center;
    font-family: "Asap Condensed", sans-serif; font-size: 13px; color: #fff; text-transform: uppercase;
  }
  .nav-item.is-active { background: var(--yellow); color: var(--text-dark); }

  /* content area */
  .content-panel { left: 76px; top: 152px; width: 885px; height: 976px; background: var(--black); }

  /* hero */
  .hero-rule { left: 100px; width: 839px; height: 2px; background: var(--yellow); }
  .hero-photo {
    left: 100px; top: 182px; width: 839px; height: 413px;
    background: linear-gradient(100deg, var(--grass-a) 0%, #c89a55 35%, var(--grass-b) 60%, #b7944e 80%, #6f7a3c 100%);
  }
  .share-dots { left: 108px; top: 188px; display: flex; gap: 7px; }
  .share-dots span { width: 10px; height: 10px; border-radius: 50%; background: rgba(255,255,255,0.85); }
  .hero-card { left: 464px; top: 295px; width: 414px; height: 300px; background: var(--panel); }
  .hero-title {
    left: 485px; top: 302px; width: 390px;
    font-size: 25px; line-height: 28.5px; font-weight: 400; color: var(--yellow);
  }
  .hero-copy { left: 485px; top: 391px; width: 278px; font-size: 11px; line-height: 13px; color: #fff; }
  .read-more {
    left: 773px; top: 554px; width: 88px; height: 21px; background: var(--red);
    border-radius: 3px; font-size: 12px; color: #fff;
    display: flex; align-items: center; justify-content: center;
  }
  .hero-bar { left: 100px; top: 595px; width: 839px; height: 32px; background: var(--hero-bar); }
  .slide-count { right: 108px; top: 606px; font-size: 10px; color: #fff; }

  /* tour cards */
  .tour-title { font-family: "Asap Condensed", sans-serif; font-size: 19px; font-weight: 400; color: #fff; top: 651px; }
  .tour-rule { top: 677px; width: 259px; height: 2px; background: var(--yellow); }
  .tour-tab { top: 658px; width: 33px; height: 13px; background: linear-gradient(90deg, #c81d1d, #f2a100 55%, var(--yellow)); }
  .tour-photo { top: 689px; width: 259px; height: 211px; }
  .photo-guided { background: linear-gradient(160deg, #d5dfe6 0%, #b58a55 45%, #8a6a3a 100%); }
  .photo-self { background: linear-gradient(160deg, #6b5a2c 0%, #c08a40 50%, #7a5a2a 100%); }
  .photo-build { background: linear-gradient(160deg, #4c5a3a 0%, #8a7a5a 50%, #b08058 100%); }

  /* about & contact */
  .info-title { top: 938px; font-family: "Asap Condensed", sans-serif; font-size: 20px; font-weight: 400; color: #fff; }
  .info-rule { top: 969px; height: 2px; background: var(--yellow); }
  .about-copy { left: 98px; top: 980px; width: 520px; font-size: 13px; line-height: 15.6px; }
  .contact-list { left: 689px; top: 980px; font-size: 13px; line-height: 15.6px; list-style: none; }

  /* footer */
  .footer-band { left: 76px; top: 1128px; width: 885px; height: 26px; background: var(--yellow); }
  .footer-copy { left: 388px; top: 1164px; font-size: 10.5px; }
  .footer-login { right: 108px; top: 1164px; font-size: 11px; }
</style>
</head>
<body>
  <header class="abs site-header"></header>
  <div class="abs brand">
    <span class="brand-mark"></span>
    <span class="brand-name">Skyward Rovers</span>
  </div>
  <p class="abs book-note">Book a first time session</p>
  <a class="abs book-button">BOOK NOW!</a>

  <nav class="abs main-nav" aria-label="Main"></nav>
  <div class="abs nav-rule"></div>
  <a class="abs nav-item is-active" style="left:99px">Home</a>
  <a class="abs nav-item" style="left:269px">About Us</a>
  <a class="abs nav-item" style="left:439px">Sample Tours</a>
  <a class="abs nav-item" style="left:609px">Testimonials</a>
  <a class="abs nav-item" style="left:779px">Sign Up</a>

  <main class="abs content-panel"></main>

  <div class="abs hero-rule" style="top:175px"></div>
  <div class="abs hero-photo" role="img" aria-label="Photo of a male lion and a lioness resting in golden grassland"></div>
  <div class="abs share-dots"><span></span><span></span><span></span></div>
  <div class="abs hero-card"></div>
  <h1 class="abs hero-title">Welcome to the world of<br>skyward rovers<br>flying safaris of a lifetime</h1>
  <p class="abs hero-copy">The most pristine and unspoiled places on every continent lie far off the beaten track, often reachable only by air. If a genuine, wild experience is what you are after, our flying safaris are waiting for you. You will not find these routes in any guidebook or airport listing. We plan every leg for you: remote airstrips, fuel stops, permits, local guides and comfortable lodges, so you can focus on the flying and the views. From savannah and desert to glaciers, rainforest and rugged coastline, bush flying combines great beauty and independence with a touch of adventure. Fly yourself as pilot in command, or sit back as our guest while an experienced bush pilot takes the controls.</p>
  <a class="abs read-more">Read More</a>
  <div class="abs hero-bar"></div>
  <span class="abs slide-count">1/1</span>
  <div class="abs hero-rule" style="top:631px"></div>

  <h2 class="abs tour-title" style="left:98px">Guided Tours</h2>
  <div class="abs tour-tab" style="left:319px"></div>
  <div class="abs tour-rule" style="left:96px"></div>
  <div class="abs tour-photo photo-guided" style="left:98px" role="img" aria-label="Photo of a giraffe under a tree"></div>

  <h2 class="abs tour-title" style="left:386px">Self-Guided Tours</h2>
  <div class="abs tour-tab" style="left:612px"></div>
  <div class="abs tour-rule" style="left:386px"></div>
  <div class="abs tour-photo photo-self" style="left:386px" role="img" aria-label="Photo of a lion with a full mane"></div>

  <h2 class="abs tour-title" style="left:677px">Build Your Trip</h2>
  <div class="abs tour-tab" style="left:902px"></div>
  <div class="abs tour-rule" style="left:677px"></div>
  <div class="abs tour-photo photo-build" style="left:677px" role="img" aria-label="Photo of two antelope sparring among trees"></div>

  <h2 class="abs info-title" style="left:98px">About Us</h2>
  <div class="abs info-rule" style="left:95px;width:564px"></div>
  <p class="abs about-copy">Skyward Rovers organises and sells flying safaris to the wildest corners of the world. What better way to see wild landscapes than from the pilot's seat of your own aircraft? Whether you're a PPL wanting to experience something beyond flying circuits at your local airfield, a seasoned ATP looking to recapture that passion for flying, or a traveller wanting to see the wild from a bird's perspective, alone or as part of a group, our journeys offer a truly rewarding and unforgettable experience.</p>

  <h2 class="abs info-title" style="left:687px">Contact Us</h2>
  <div class="abs info-rule" style="left:687px;width:244px"></div>
  <ul class="abs contact-list">
    <li>Tomas Brenner</li>
    <li>+41 70 555 01 23</li>
    <li>Bern, Switzerland</li>
    <li>info@skyward-rovers.example</li>
  </ul>

  <footer class="abs footer-band"></footer>
  <p class="abs footer-copy">© 2013 by Daniel Fairbrook. All rights reserved</p>
  <a class="abs footer-login">Webmaster Login</a>
</body>
</html>
```